Condo Debts Collection Business needs a Web Design (Contest)

I need a site for a client, who works with condo debts collection, and ensure all revenues provided by condo fees will be always available to the building manager of condo on a specific date, regardless of defaults.I have the logo of the companies, and some requirements on layout (kind of slider, menu options, phone number on a noble position, etc).
Updates

Designs look the same

Target Market(s)

I have two targets for this design: - Condominium's building manager. This target is looking for a solution to overdue debts on it's condo. - Residents on condominiums. This target wants to live in a better place, where their neighbors pay their condominium fees on time.

Number of Pages Required

1 page

Requirements
Must have
• - Slider with title, some short text related, a nice image (I prefer happy and/or peaceful family, people doing business, happy friends, and so on).
• - I have a special attention to menu. I'm looking for one I can have a nice effect, more elegant, charming, kind of innovative.
• - Phone number on the top (or clearly visible).
• - Member log in area or icon on the top (or clearly visible).
• - News/articles area.
• - Modern fonts, with good quality, sans-serif on areas where reading is more intensive (prefer Google web-fonts).
• - Colors specified on attached files.
• - Header similar or inspired by the "FILE 3"
Nice to have
• - Clear background color, cause it's better to read larger texts (like articles). Dark backgrounds makes reading difficult.
• - A site with effects (like shadows, lines, gradients, lights) is usually pretty.
• - I pay attention on beautiful footers.
Should not have
• - Images with a lot of money (I don't sell richness, I sell tranquility, peace, harmony, safety).
• - Poor menu.
• - Lots of curves. My customer asked for straight lines.

```html
<!DOCTYPE html>
<html lang="en">
<head>
<meta charset="utf-8">
<title>Serenara</title>
<link href="https://fonts.googleapis.com/css2?family=Montserrat:wght@400;500;600;700&display=swap" rel="stylesheet">
<style>
:root{
  --navy:#0d3a78;
  --navy-dark:#0a2c5c;
  --navy-deep:#08244d;
  --blue:#0a4f9f;
  --orange:#e57b1c;
  --white:#ffffff;
  --input:#d3dae4;
}
*{margin:0;padding:0;box-sizing:border-box}
html,body{width:857px;height:1200px;overflow:hidden}
body{font-family:'Montserrat',sans-serif;color:var(--navy);background:var(--white);position:relative}
.abs{position:absolute}

.site-header{position:absolute;left:0;top:0;width:857px;height:80px;background:linear-gradient(90deg,#0e438a,var(--navy) 40%)}
.brand{position:absolute;left:34px;top:28px;display:flex;align-items:center;gap:8px;color:var(--white);font-weight:700;font-size:17px;letter-spacing:.3px}
.brand-mark{width:18px;height:18px;background:var(--orange)}
.main-nav{position:absolute;top:36px;left:418px;display:flex;gap:0}
.main-nav a{font-size:8px;font-weight:700;letter-spacing:1.4px;color:var(--white);text-decoration:none;position:absolute;white-space:nowrap}
.main-nav a.active::after{content:"";position:absolute;left:4px;right:4px;top:14px;height:2px;background:var(--orange)}
.login-btn{position:absolute;left:704px;top:26px;width:153px;height:29px;background:var(--orange);clip-path:polygon(0 0,100% 0,100% 100%,4% 100%);color:var(--white);font-size:8px;font-weight:700;letter-spacing:1.3px;display:flex;align-items:center;padding-left:30px}
.login-btn svg{position:absolute;left:14px;top:8px}

.hero{position:absolute;left:0;top:80px;width:857px;height:354px;overflow:hidden}
.hero-photo{position:absolute;inset:0;background:linear-gradient(120deg,#2f5f6e 0%,#8d6a58 40%,#d9b8a2 65%,#b8c7d6 100%)}
.hero-panel{position:absolute;inset:0;background:var(--orange);clip-path:polygon(0 0,336px 0,268px 354px,0 354px)}
.hero-title{position:absolute;left:66px;top:68px;font-size:39px;line-height:40px;font-weight:700;color:var(--white);letter-spacing:-.3px}
.hero-sub{position:absolute;left:68px;top:196px;width:220px;font-size:12.5px;line-height:17px;font-weight:700;color:var(--navy)}
.btn-navy{position:absolute;left:68px;top:261px;width:120px;height:28px;background:var(--navy);color:var(--white);font-size:8px;font-weight:700;letter-spacing:1.3px;display:flex;align-items:center;justify-content:center}
.hero-phone{position:absolute;left:588px;top:309px;width:269px;height:45px;background:var(--navy);clip-path:polygon(10px 0,100% 0,100% 100%,0 100%);color:var(--white);font-size:15px;font-weight:700;display:flex;align-items:center;padding-left:37px;gap:8px}

.intro{position:absolute;left:140px;top:468px;width:577px;text-align:center;font-size:11.5px;line-height:17px;font-weight:700;color:var(--navy)}

.about{position:absolute;left:0;top:530px;width:857px;height:304px;background:linear-gradient(180deg,#eef2f7 0,#fff 30px)}
.about-text{position:absolute;left:68px;top:50px;width:362px;font-size:9.6px;line-height:15.5px;color:var(--navy)}
.about-text p+p{margin-top:15px}
.btn-orange{position:absolute;height:28px;background:var(--orange);color:var(--white);font-size:7.8px;font-weight:700;letter-spacing:1.4px;display:flex;align-items:center;justify-content:center}
.about-photo{position:absolute;left:428px;top:45px;width:429px;height:259px;background:linear-gradient(135deg,#6b3b24 0%,#8a5033 35%,#e7eaf2 60%,#4aa3d8 80%,#6b3b24 100%);clip-path:polygon(40% 0,100% 18%,100% 100%,0 100%)}

.news{position:absolute;left:0;top:834px;width:857px;height:240px;background:linear-gradient(180deg,var(--blue),#0d3d7c)}
.news h2{position:absolute;left:0;width:857px;top:36px;text-align:center;font-size:15px;font-weight:700;color:var(--white)}
.news-item{position:absolute;top:78px;width:225px;color:var(--white)}
.news-date{font-size:7.5px;font-weight:500}
.news-title{font-size:9.2px;font-weight:700;letter-spacing:1.5px;color:var(--orange);margin-top:4px}
.news-body{font-size:9.8px;line-height:15.5px;margin-top:6px}
.news-item .btn-orange{position:relative;width:92px;height:23px;margin-top:10px}
.news-divider{position:absolute;top:76px;width:1px;height:120px;background:rgba(255,255,255,.25)}

.site-footer{position:absolute;left:0;top:1074px;width:857px;height:97px;background:var(--navy-deep)}
.footer-panel{position:absolute;inset:0;background:var(--navy-dark);clip-path:polygon(0 0,378px 0,358px 100%,0 100%)}
.social{position:absolute;left:34px;top:28px;display:flex;flex-direction:column;gap:9px}
.social span{width:9px;height:9px;background:var(--white);border-radius:50%}
.social-rule{position:absolute;left:60px;top:24px;width:1px;height:53px;background:rgba(255,255,255,.35)}
.address{position:absolute;left:77px;top:28px;width:280px;font-size:7px;line-height:11px;color:var(--white)}
.address .line{margin-top:4px}
.address .mail{color:var(--orange);font-weight:700;margin-top:4px}
.newsletter h3{position:absolute;left:423px;top:29px;font-size:9.3px;font-weight:700;letter-spacing:1.6px;color:var(--white)}
.field{position:absolute;top:47px;width:160px;height:22px;background:var(--input);font-size:8px;font-weight:700;color:var(--navy);padding-left:10px;display:flex;align-items:center}
.bottom-bar{position:absolute;left:0;top:1171px;width:857px;height:29px;background:var(--orange);color:var(--white)}
.copyright{position:absolute;left:34px;top:11px;font-size:6.5px}
.bottom-nav{position:absolute;right:34px;top:11px;display:flex;gap:19px;font-size:7px;font-weight:700;letter-spacing:1.2px}
</style>
</head>
<body>

<header class="site-header">
  <div class="brand"><span class="brand-mark"></span>SERENARA</div>
  <nav class="main-nav">
    <a class="active" style="left:0">HOME</a>
    <a style="left:62px">ABOUT US</a>
    <a style="left:146px">NEWS</a>
    <a style="left:207px">CONTACT</a>
  </nav>
  <div class="login-btn">
    <svg width="10" height="13" viewBox="0 0 10 13"><circle cx="5" cy="3.5" r="3" fill="#fff"/><path d="M0 13 C0 8 10 8 10 13Z" fill="#fff"/></svg>
    ACCOUNT LOGIN
  </div>
</header>

<section class="hero">
  <div class="hero-photo" role="img" aria-label="Photo of a smiling family: mother, father and young child together at home"></div>
  <div class="hero-panel"></div>
  <h1 class="hero-title">Garantindo a<br>tranquilidade do<br>seu condominio</h1>
  <p class="hero-sub">Lorem ipsum dolor sit amet, consectetur adipiscing eiusmod tempor ut dolore magna aliqua.</p>
  <div class="btn-navy">FIND OUT MORE</div>
  <div class="hero-phone">
    <svg width="18" height="18" viewBox="0 0 18 18"><circle cx="9" cy="9" r="9" fill="var(--orange)"/><path d="M6 4.5l2 2-1 1.3c.6 1.3 1.6 2.3 2.9 2.9l1.3-1 2 2-1.2 1.5c-3.5-.3-6.5-3.3-6.8-6.8z" fill="#fff"/></svg>
    4187-2210 / 4187-2290
  </div>
</section>

<p class="intro">Lorem ipsum dolor sit amet, consectetur adipiscing elit, sed do eiusmod tempor incididunt ut labore et dolore magna aliqua. Ut enim ad minim veniam, quis nostrud exercitatio</p>

<section class="about">
  <div class="about-text">
    <p>Lorem ipsum dolor sit amet, consectetur adipiscing elit, sed do eiusmod tempor incididunt ut labore et dolore magna aliqua. Ut enim ad minim veniam, quis nostrud exercitation ullamco laboris nisi ut aliquip ex ea commodo consequat. Duis aute irure dolor in reprehenderit in voluptate velit esse cillum dolore eu fugiat nulla pariatur.</p>
    <p>Sed ut perspiciatis unde omnis iste natus error sit voluptatem accusantium doloremque laudantium, totam rem aperiam, eaque ipsa quae ab illo inventore veritatis et quasi architecto beatae vitae dicta sunt explicabo.</p>
  </div>
  <div class="btn-orange" style="left:68px;top:216px;width:183px">I AM A BUILDING MANAGER</div>
  <div class="btn-orange" style="left:274px;top:216px;width:131px">I AM A RESIDENT</div>
  <div class="about-photo" role="img" aria-label="Photo of a modern apartment building with wooden balcony screens seen from below"></div>
</section>

<section class="news">
  <h2>Latest News</h2>
  <article class="news-item" style="left:68px">
    <div class="news-date">23 March 2019</div>
    <div class="news-title">NEWS ARTICLE TITLE</div>
    <p class="news-body">Quis nostrud exercitation ullamco laboris nisi ut aliquip ex ea commodo consequat. Duis aute irure dolor in reprehenderit ...</p>
    <div class="btn-orange" style="left:2px">READ MORE</div>
  </article>
  <div class="news-divider" style="left:303px"></div>
  <article class="news-item" style="left:323px">
    <div class="news-date">23 March 2019</div>
    <div class="news-title">NEWS ARTICLE TITLE</div>
    <p class="news-body">Duis aute irure dolor reprehenderit voluptate velit esse cillum dolore eu fugiat nulla pariatu excepteur sint occaecat cupidatat ...</p>
    <div class="btn-orange" style="left:1px">READ MORE</div>
  </article>
  <div class="news-divider" style="left:554px"></div>
  <article class="news-item" style="left:575px">
    <div class="news-date">23 March 2019</div>
    <div class="news-title">NEWS ARTICLE TITLE</div>
    <p class="news-body">Excepteur sint occaecat cupidatat proident, sunt in culpa qui officia deserunt mollit anim id est laborum unde omnis iste natus ...</p>
    <div class="btn-orange" style="left:1px">READ MORE</div>
  </article>
</section>

<footer class="site-footer">
  <div class="footer-panel"></div>
  <div class="social"><span></span><span></span><span></span></div>
  <div class="social-rule"></div>
  <div class="address">
    <div>Rua das Acácias Brancas, 415, Centro Comercial Horizonte, sala 602 - Vila Nova - Sao Jose - SC CEP 88 104-300</div>
    <div class="line">4187-2210 / 4187-2290</div>
    <div class="mail">contato@serenara.com.br</div>
  </div>
  <div class="newsletter">
    <h3>SIGN UP TO OUR NEWSLETTER</h3>
    <div class="field" style="left:423px">Name</div>
    <div class="field" style="left:594px">Email Address</div>
    <div class="btn-orange" style="left:765px;top:47px;width:57px;height:22px">SIGNUP</div>
  </div>
</footer>

<div class="bottom-bar">
  <div class="copyright">© Copyright 2019 Lumen Studio</div>
  <nav class="bottom-nav"><span>HOME</span><span>ABOUT US</span><span>RESIDENTS</span><span>CONTACT US</span><span>ACCOUNT LOGIN</span></nav>
</div>

</body>
</html>
```